Ancient Art and Artifact information website

Hello Designers,
We are starting up a new website who talk abut and discusses an ancient arts artifacts. We would covering a wide range of countries ranging from Egypt, Greece, India, Syria, Rome, etc. My website name Brisk Loom
Designs that fits with ancient theme and some kind of uniqueness would be accepted.
Requirements:
1) A home page design
2) Sub page design
3) A suitable logo
Sections can be added are featured ancient arts/places with short description followed by a more button, latest news, and comment section.
Add contents if you found relevant for this category of website. Ability to share the information through social media is desired.
Must be a responsive design. I look forward to designs which are mind blowing.
2 page

```html
<!DOCTYPE html>
<html lang="en">
<head>
<meta charset="utf-8">
<title>Brisk Loom — Ancient Arts Artifacts</title>
<link href="https://fonts.googleapis.com/css2?family=Mulish:wght@300;400;600;700&display=swap" rel="stylesheet">
<style>
:root{
  --coral:#f25a55;
  --coral-dark:#5a0c0c;
  --ink:#1c1c1c;
  --body:#7a7a7a;
  --grey-band:#e4e4e4;
  --white:#ffffff;
  --footer:#050505;
}
*{box-sizing:border-box;margin:0;padding:0}
html,body{width:1200px;height:3046px;overflow:hidden}
body{font-family:"Mulish",sans-serif;background:var(--white);color:var(--ink);position:relative}
.abs{position:absolute}

/* hero */
.hero{left:0;top:0;width:1200px;height:694px;
  background:
    radial-gradient(ellipse 520px 260px at 420px 300px,rgba(214,180,128,.85),rgba(214,180,128,0) 70%),
    radial-gradient(ellipse 300px 240px at 1010px 380px,rgba(196,160,110,.8),rgba(196,160,110,0) 70%),
    radial-gradient(ellipse 700px 200px at 600px 640px,rgba(110,92,72,.9),rgba(110,92,72,0) 75%),
    radial-gradient(ellipse 260px 120px at 1050px 120px,rgba(235,240,250,.7),rgba(235,240,250,0) 70%),
    linear-gradient(180deg,#2f5cb5 0%,#5f86cf 22%,#a8946f 46%,#b89c74 62%,#8f7657 80%,#5b4630 100%)}
.hero-shade{left:0;top:0;width:1200px;height:694px;background:linear-gradient(180deg,rgba(0,0,0,.15),rgba(0,0,0,.05) 40%,rgba(0,0,0,.2))}
.brand{left:81px;top:38px;font-size:44px;font-weight:400;color:var(--white);letter-spacing:.5px}
.nav{top:44px;left:412px;display:flex;list-style:none}
.nav li{font-size:16px;font-weight:600;color:var(--white);padding:9px 18px;margin-right:8px;text-transform:uppercase;letter-spacing:.3px}
.nav li.active{border:2px solid var(--white)}
.hero-title{left:0;width:1200px;top:298px;text-align:center;font-size:44px;font-weight:700;color:var(--white);letter-spacing:.5px}
.hero-sub{left:245px;width:710px;top:356px;text-align:center;font-size:24px;line-height:32px;color:var(--white)}
.btn-outline{left:502px;top:438px;width:198px;height:43px;border:2px solid var(--white);color:var(--white);font-size:17px;font-weight:600;display:flex;align-items:center;justify-content:center}
.dots{left:558px;top:650px;display:flex;gap:8px}
.dots span{width:16px;height:16px;border-radius:50%;background:var(--white)}
.dots span.off{background:transparent;border:2px solid var(--white)}

/* welcome */
.welcome-small{left:79px;top:760px;font-size:28px;font-weight:400}
.welcome-big{left:79px;top:788px;font-size:52px;font-weight:400;color:var(--coral)}
.welcome-text{left:79px;width:515px;font-size:16px;line-height:25px;color:var(--body)}
.bust{left:660px;top:712px;width:400px;height:390px;border-radius:46% 46% 12% 12%;
  background:
    radial-gradient(ellipse 90px 120px at 50% 26%,#ecebe8 0%,#d4d0ca 60%,rgba(212,208,202,0) 100%),
    radial-gradient(ellipse 210px 150px at 50% 82%,#c29f7a 0%,#9c7a58 55%,rgba(156,122,88,0) 100%),
    linear-gradient(180deg,#ffffff 0%,#f3f1ee 40%,#e8ddd0 100%)}

/* dark band */
.sculpture-band{left:0;top:1100px;width:1200px;height:460px}
.band-title{left:0;width:1200px;top:1218px;text-align:center;font-size:32px;font-weight:400;color:var(--white)}
.band-text{left:178px;width:844px;top:1268px;text-align:center;font-size:16px;line-height:24px;color:#eee}
.btn-solid{background:var(--coral);color:var(--white);font-size:16px;font-weight:700;display:flex;align-items:center;justify-content:center;text-transform:uppercase}

/* featured */
.featured-title{left:0;width:1200px;top:1590px;text-align:center;font-size:27px;font-weight:400}
.card{top:1673px;width:327px;height:373px;background:var(--white);box-shadow:0 6px 14px rgba(0,0,0,.25)}
.card-img{width:327px;height:184px}
.card h3{margin:24px 32px 0;font-size:19px;font-weight:400}
.card p{margin:10px 32px 0;font-size:13px;line-height:20px;color:var(--body)}
.card .more{display:block;margin:10px 32px 0;font-size:13px;font-weight:600;color:var(--coral)}

/* news */
.news-title{left:89px;top:2220px;font-size:28px;font-weight:400}
.news{width:320px;top:2282px}
.news h4{width:265px;font-size:17px;line-height:24px;font-weight:400;color:var(--coral)}
.news p{margin-top:14px;font-size:12px;line-height:19px;color:var(--body)}
.news .read{display:block;margin-top:8px;font-size:12px;font-weight:600;color:var(--ink)}

/* comments */
.comment-title{left:0;width:1200px;top:2588px;text-align:center;font-size:28px;font-weight:400;color:var(--white)}
.comment-box{left:238px;top:2650px;width:745px;height:138px;border:1px solid rgba(255,255,255,.8);border-radius:4px;padding:12px 14px;font-size:15px;color:var(--white)}
.post-btn{left:887px;top:2796px;width:96px;height:38px;background:var(--coral-dark);color:var(--white);font-size:15px;font-weight:600;display:flex;align-items:center;justify-content:center}

/* footer */
.footer{left:0;top:2883px;width:1200px;height:163px;background:var(--footer)}
.foot-nav{left:73px;top:2932px;display:flex;list-style:none}
.foot-nav li{font-size:14px;font-weight:600;color:var(--white);margin-right:32px;text-transform:uppercase}
.copy{left:73px;top:2962px;font-size:12px;color:#777}
.social{left:973px;top:2924px;display:flex;gap:4px}
.social svg{width:34px;height:34px;display:block}
</style>
</head>
<body>

<!-- hero -->
<div class="abs hero" role="img" aria-label="Photo of a ruined ancient Greek temple with columns under a blue sky"></div>
<div class="abs hero-shade"></div>
<div class="abs brand">Brisk Loom</div>
<ul class="abs nav">
  <li class="active">Home</li><li>About us</li><li>Ancient art</li><li>News</li><li>Top places</li><li>Contact</li>
</ul>
<h1 class="abs hero-title">ANCIENT ARTS ARTIFACTS</h1>
<p class="abs hero-sub">Ut nisi erat fermentum vel congue id euismod in elit Fusce ultricies orci ac feugiat suscipit</p>
<div class="abs btn-outline">VIEW ARTS</div>
<div class="abs dots"><span class="off"></span><span></span><span></span><span></span></div>

<!-- welcome -->
<div class="abs welcome-small">WELCOME TO</div>
<div class="abs welcome-big">BRISK LOOM</div>
<p class="abs welcome-text" style="top:858px">Curabitur vel mi sit amet magna malesuada ultrices Ut nisi erat fermentum vel congue id euismo</p>
<p class="abs welcome-text" style="top:928px">Fusce ultricies orci ac feugiat suscipit leo massa sodales velit et scelerisque mi tortor at ipsum cligula augue bibendum accumsan vestibulum ut commodo</p>
<div class="abs bust" role="img" aria-label="Photo of a marble Roman bust sculpture"></div>

<!-- dark band -->
<svg class="abs sculpture-band" width="1200" height="460" viewBox="0 0 1200 460" role="img" aria-label="Dark photo of terracotta warrior sculptures">
  <defs>
    <linearGradient id="bronze" x1="0" y1="0" x2="1" y2="1">
      <stop offset="0" stop-color="#3e2f22"/><stop offset=".45" stop-color="#6e5540"/><stop offset=".75" stop-color="#5a4432"/><stop offset="1" stop-color="#2a1f16"/>
    </linearGradient>
    <radialGradient id="glow1" cx=".2" cy=".55" r=".35"><stop offset="0" stop-color="#9a7a5c" stop-opacity=".7"/><stop offset="1" stop-color="#9a7a5c" stop-opacity="0"/></radialGradient>
    <radialGradient id="glow2" cx=".82" cy=".4" r=".3"><stop offset="0" stop-color="#a3826a" stop-opacity=".6"/><stop offset="1" stop-color="#a3826a" stop-opacity="0"/></radialGradient>
  </defs>
  <polygon points="0,40 95,10 170,60 380,20 530,50 760,35 900,0 1200,40 1200,420 1060,450 760,425 520,460 300,420 0,445" fill="url(#bronze)"/>
  <polygon points="0,40 95,10 170,60 380,20 530,50 760,35 900,0 1200,40 1200,420 1060,450 760,425 520,460 300,420 0,445" fill="url(#glow1)"/>
  <polygon points="0,40 95,10 170,60 380,20 530,50 760,35 900,0 1200,40 1200,420 1060,450 760,425 520,460 300,420 0,445" fill="url(#glow2)"/>
  <polygon points="0,40 95,10 170,60 380,20 530,50 760,35 900,0 1200,40 1200,420 1060,450 760,425 520,460 300,420 0,445" fill="rgba(0,0,0,.2)"/>
</svg>
<h2 class="abs band-title">TOP ANCIENT ARTS ARTIFACTS</h2>
<p class="abs band-text">Integer congue augue et malesuada iaculis ipsum dui aliquet felis at cursus magna nisl nec elit Praesent elementum elit at tellus nec ultricies sit amet porttitor mattis enim In massa est eget tempor cursus neque mi consectetuer mi a ultricies massa est sed nisl Class aptent taciti sociosqu</p>
<div class="abs btn-solid" style="left:506px;top:1364px;width:196px;height:45px">View more</div>

<!-- featured grey band -->
<svg class="abs" style="left:0;top:1520px" width="1200" height="690" viewBox="0 0 1200 690">
  <polygon points="0,52 300,62 520,66 760,40 1060,58 1200,34 1200,640 940,672 760,655 520,690 300,660 0,672" fill="var(--grey-band)"/>
</svg>
<h2 class="abs featured-title">FEATURED ANCIENT ARTS</h2>

<article class="abs card" style="left:73px">
  <div class="card-img" role="img" aria-label="Photo of a large bronze head sculpture among temple ruins" style="background:radial-gradient(ellipse 120px 70px at 55% 60%,#8c8a5a,rgba(140,138,90,0) 80%),linear-gradient(180deg,#d8c49a 0%,#b89e6a 45%,#6f6a3c 75%,#4b5a2a 100%)"></div>
  <h3>Ancient Art Tittle here</h3>
  <p>Curabitur vel mi sit amet magna malesu ada ultrices Ut nisi erat fermentum vel congue id euismod in elit Fusce aultricies orci ac feugiat suscipit</p>
  <span class="more">LEARN MORE</span>
</article>
<article class="abs card" style="left:422px">
  <div class="card-img" role="img" aria-label="Photo of a carved marble relief of a standing figure" style="background:radial-gradient(ellipse 80px 100px at 48% 55%,#f2e6d2,rgba(242,230,210,0) 80%),linear-gradient(160deg,#e6d2b0,#c9ad82 55%,#a88a60)"></div>
  <h3>Ancient Art Tittle here</h3>
  <p>Curabitur vel mi sit amet magna malesu ada ultrices Ut nisi erat fermentum vel congue id euismod in elit Fusce aultricies orci ac feugiat suscipit</p>
  <span class="more">LEARN MORE</span>
</article>
<article class="abs card" style="left:773px">
  <div class="card-img" role="img" aria-label="Photo of a lit wooden horse monument under a night sky" style="background:radial-gradient(circle 20px at 18% 22%,#d9502e,rgba(217,80,46,0) 100%),radial-gradient(ellipse 90px 80px at 62% 55%,#c98a3c,rgba(201,138,60,0) 85%),linear-gradient(180deg,#18298a,#3550b5 60%,#6b6aa0 85%,#a0783a)"></div>
  <h3>Ancient Art Tittle here</h3>
  <p>Curabitur vel mi sit amet magna malesu ada ultrices Ut nisi erat fermentum vel congue id euismod in elit Fusce aultricies orci ac feugiat suscipit</p>
  <span class="more">LEARN MORE</span>
</article>
<div class="abs btn-solid" style="left:493px;top:2075px;width:197px;height:46px">View more</div>

<!-- latest news -->
<h2 class="abs news-title">LATEST NEWS</h2>
<article class="abs news" style="left:89px">
  <h4>Morbi diam mauris viverra in gravida eu mattis in ante</h4>
  <p>Ut nisi erat fermentum vel congue id euismod in elit Fusce ultricies orci ac feugiat suscipit leo massa sodales velit et scelerisque</p>
  <span class="read">READ MORE</span>
</article>
<article class="abs news" style="left:453px">
  <h4>Morbi diam mauris viverra in gravida eu mattis in ante</h4>
  <p>Ut nisi erat fermentum vel congue id euismod in elit Fusce ultricies orci ac feugiat suscipit leo massa sodales velit et scelerisque</p>
  <span class="read">READ MORE</span>
</article>
<article class="abs news" style="left:822px;top:2274px">
  <h4>Morbi diam mauris viverra in gravida eu mattis in ante</h4>
  <p>Ut nisi erat fermentum vel congue id euismod in elit Fusce ultricies orci ac feugiat suscipit leo massa sodales velit et scelerisque</p>
  <span class="read">READ MORE</span>
</article>

<!-- comments -->
<svg class="abs" style="left:0;top:2510px" width="1200" height="380" viewBox="0 0 1200 380">
  <polygon points="0,34 170,20 360,40 520,10 700,34 1200,24 1200,380 0,380" fill="var(--coral)"/>
</svg>
<h2 class="abs comment-title">POST YOUR COMMENTS</h2>
<div class="abs comment-box">Type Your Comment</div>
<div class="abs post-btn">POST</div>

<!-- footer -->
<footer class="abs footer"></footer>
<ul class="abs foot-nav">
  <li>Home</li><li>About us</li><li>Ancient art</li><li>News</li><li>Top places</li><li>Contact</li>
</ul>
<div class="abs copy">© 2017 Company Name &nbsp;All right reserved &nbsp;Term of Use</div>
<div class="abs social" aria-label="Share links">
  <!-- share -->
  <svg viewBox="0 0 34 34" aria-label="Share"><circle cx="17" cy="17" r="16" fill="none" stroke="#fff" stroke-width="1.6"/><circle cx="12" cy="17" r="2.4" fill="#fff"/><circle cx="22" cy="11.5" r="2.4" fill="#fff"/><circle cx="22" cy="22.5" r="2.4" fill="#fff"/><path d="M12 17 22 11.5M12 17 22 22.5" stroke="#fff" stroke-width="1.5"/></svg>
  <!-- mail -->
  <svg viewBox="0 0 34 34" aria-label="Email"><circle cx="17" cy="17" r="16" fill="none" stroke="#fff" stroke-width="1.6"/><rect x="10" y="12" width="14" height="10" fill="none" stroke="#fff" stroke-width="1.5"/><path d="M10 12 17 18 24 12" fill="none" stroke="#fff" stroke-width="1.5"/></svg>
  <!-- link -->
  <svg viewBox="0 0 34 34" aria-label="Copy link"><circle cx="17" cy="17" r="16" fill="none" stroke="#fff" stroke-width="1.6"/><rect x="9" y="14.5" width="9" height="5" rx="2.5" fill="none" stroke="#fff" stroke-width="1.5"/><rect x="16" y="14.5" width="9" height="5" rx="2.5" fill="none" stroke="#fff" stroke-width="1.5"/></svg>
  <!-- heart -->
  <svg viewBox="0 0 34 34" aria-label="Like"><circle cx="17" cy="17" r="16" fill="none" stroke="#fff" stroke-width="1.6"/><path d="M17 23.5 11 17.5a3.3 3.3 0 0 1 6-4 3.3 3.3 0 0 1 6 4z" fill="#fff"/></svg>
</div>

</body>
</html>
```